CD cover "Marisol Quintero"

Here I send the pictures for the cover, leaving creative freedom to the photography and any modifications you make. The artist is called Marisol Quintero, and the title of the album is called. "Over Quiet Rivers" but please translate that to Spanish. Thank you for your valuable work.
The name of the artist is: Marisol Quintero
Album Name: “Sobre ríos quietos” in Spanish

```html
<!DOCTYPE html>
<html lang="es">
<head>
<meta charset="utf-8">
<title>Sobre ríos quietos — Marisol Quintero</title>
<link rel="stylesheet" href="https://fonts.googleapis.com/css2?family=Allura&family=Poppins:wght@400&display=swap">
<style>
  :root {
    --orange: #f0852a;
    --orange-mid: #f39a26;
    --amber: #f8bb20;
    --yellow: #fde800;
    --frame: #ffffff;
    --title: #ffffff;
    --title-shadow: #1a1a1a;
    --artist: #1c1c1c;
  }
  html, body {
    margin: 0;
    padding: 0;
    width: 1200px;
    height: 1200px;
    overflow: hidden;
    background: #d9d9d9;
  }
  .cover {
    position: relative;
    width: 1200px;
    height: 1200px;
    background: linear-gradient(135deg, var(--orange) 0%, var(--orange) 30%, var(--orange-mid) 50%, var(--amber) 72%, var(--yellow) 100%);
    overflow: hidden;
  }
  .cover__frame {
    position: absolute;
    left: 30px;
    top: 30px;
    right: 30px;
    bottom: 30px;
    border: 7px solid var(--frame);
    box-sizing: border-box;
  }
  .cover__photo {
    position: absolute;
    left: 0;
    top: 0;
    width: 1200px;
    height: 1200px;
  }
  .cover__title {
    position: absolute;
    left: 0;
    width: 100%;
    top: 900px;
    margin: 0;
    text-align: center;
    font-family: "Allura", cursive;
    font-weight: 400;
    font-size: 124px;
    line-height: 1;
    color: var(--title);
    text-shadow: 3px 3px 0 var(--title-shadow);
  }
  .cover__artist {
    position: absolute;
    left: 0;
    width: 100%;
    top: 1068px;
    margin: 0;
    text-align: center;
    font-family: "Poppins", sans-serif;
    font-weight: 400;
    font-size: 48px;
    line-height: 1;
    color: var(--artist);
  }
</style>
</head>
<body>
  <main class="cover">
    <div class="cover__frame"></div>

    <svg class="cover__photo" viewBox="0 0 1200 1200" role="img" aria-label="Photograph in a brush-stroke shape: a woman in a long blue dress walking away along a dirt path between dry grass hills under a pale sky">
      <defs>
        <linearGradient id="photo-tones" x1="0" y1="0" x2="0" y2="1" gradientUnits="userSpaceOnUse" gradientTransform="scale(1200)">
          <stop offset="0.12" stop-color="#e6e8ef"/>
          <stop offset="0.42" stop-color="#d9d4cf"/>
          <stop offset="0.50" stop-color="#7f8a5c"/>
          <stop offset="0.60" stop-color="#9c907c"/>
          <stop offset="0.75" stop-color="#a89a84"/>
          <stop offset="0.90" stop-color="#c9b491"/>
        </linearGradient>
      </defs>
      <polygon fill="url(#photo-tones)" points="
        137,578 205,545 190,530 260,500 300,455 345,430 330,418 395,380
        400,318 460,310 430,300 510,285 540,255 600,238 560,232 640,200
        615,190 673,150 700,172 720,162 760,178 800,158 850,168 830,150
        900,140 960,160 980,150 1070,327 1000,355 1040,370 985,398
        1010,415 955,440 975,458 920,490 940,505 880,540 900,560 840,585
        862,602 800,640 820,660 760,700 780,715 715,760 735,780 673,837
        640,845 600,870 560,860 520,880 470,872 405,880 430,850 375,845
        400,820 330,810 350,790 290,770 310,745 250,735 275,710 215,690
        240,665 185,640 205,615 160,605"/>
    </svg>

    <h1 class="cover__title">Sobre ríos quietos</h1>
    <p class="cover__artist">Marisol Quintero</p>
  </main>
</body>
</html>
```